Mobile phone signal boosting solutions needs a website

We need a website design for the reselling of a mobile signal boosting product set. These solutions are Vexlor exempt and will provide an indoor signal for mobile phones. We would like to see designs that incorporate the colours and feel of our logo. The domain will be
openmeadow.com / co.uk
Overview of the company and how it is to be used: Open meadow (domain name) will work with business and end user to provide mobile signal boosting – where people struggle indoors with a mobile signal our solutions will help by finding the smallest signal and boosting it, allowing users to use voice and data over their mobile network (please note this is not wireless signal boosting)
Number of Pages:
-Home
-Solutions / How it works
-Case Studies
-Contact
Text content: Currently just use placeholders
Technical specs : Wordpress and ability to use CMS if that’s relevant
Target Market(s)
Business professional all markets /high end residential
Coded - Design and coding required
4 page

```html
<!DOCTYPE html>
<html lang="en">
<head>
<meta charset="utf-8">
<title>Open meadow – Mobile Signal Boosting</title>
<link rel="stylesheet" href="https://fonts.googleapis.com/css2?family=Inter:wght@400;500;600;700&display=swap">
<style>
:root{
  --yellow:#fcc400;
  --yellow-deep:#f2b400;
  --ink:#1b1b1b;
  --text:#2a2a2a;
  --cream:#f7f1e2;
  --field:#f1f1f1;
  --white:#ffffff;
  --footer:#0b0b0b;
}
*{box-sizing:border-box;margin:0;padding:0}
html,body{width:1200px;height:3245px;overflow:hidden}
body{position:relative;background:var(--white);font-family:"Inter",Arial,sans-serif;color:var(--text)}
.btn{position:absolute;display:flex;align-items:center;justify-content:center;background:var(--yellow);color:var(--ink);font-weight:700;font-size:12.5px;letter-spacing:.2px;border-radius:7px;border:1px solid #c99a00;text-decoration:none;white-space:nowrap}
.btn-outline{background:transparent;border:1.5px solid #b98f00}
/* header */
.site-header{position:absolute;left:0;top:0;width:1200px;height:68px;background:var(--white)}
.brand-card{position:absolute;left:147px;top:0;width:164px;height:147px;background:var(--white);border-radius:0 0 12px 12px;box-shadow:0 6px 14px rgba(0,0,0,.18);display:flex;flex-direction:column;align-items:center;justify-content:center;gap:10px;z-index:3}
.brand-mark{width:22px;height:22px;background:var(--yellow)}
.brand-name{font-weight:700;font-size:19px;color:var(--ink);white-space:nowrap}
.main-nav a{position:absolute;top:31px;font-size:13.5px;color:var(--ink);text-decoration:none}
.main-nav a.active::after{content:"";position:absolute;left:0;right:0;bottom:-6px;height:1.5px;background:#bdbdbd}
/* hero */
.hero{position:absolute;left:0;top:68px;width:1200px;height:540px;background:var(--yellow)}
.hero-photo{position:absolute;left:540px;top:0;width:660px;height:540px;background:linear-gradient(90deg,rgba(252,196,0,1) 0%,rgba(242,200,90,.85) 30%,#d9b27a 60%,#e8e6e2 100%)}
.hero h1{position:absolute;left:147px;top:115px;font-size:42px;line-height:49px;font-weight:500;color:var(--ink);letter-spacing:.2px;white-space:nowrap}
.hero p{position:absolute;left:147px;top:229px;width:390px;font-size:17px;line-height:23px;color:var(--ink)}
.service-card{position:absolute;top:490px;width:324px;height:213px;background:var(--white);border-radius:14px;box-shadow:0 18px 40px rgba(0,0,0,.12);text-align:center;z-index:2}
.service-card h3{font-size:19.5px;font-weight:500;color:var(--ink);margin-top:8px}
.service-card p{font-size:13px;line-height:21.5px;color:var(--text);margin-top:14px;padding:0 30px}
/* about */
.about-logo{position:absolute;left:200px;top:800px;width:320px;text-align:center}
.about-logo .mark{width:60px;height:60px;background:var(--yellow);margin:0 auto 40px}
.about-logo .name{font-size:44px;font-weight:700;color:var(--ink);letter-spacing:-1px;white-space:nowrap}
.eyebrow{position:absolute;left:628px;top:794px;font-size:15.5px;font-weight:600;color:var(--yellow)}
.about h2{position:absolute;left:628px;top:822px;width:420px;font-size:27px;line-height:33px;font-weight:500;color:var(--ink)}
.about p{position:absolute;left:628px;top:894px;width:395px;font-size:13px;line-height:21.5px}
/* product */
.product{position:absolute;left:0;top:1130px;width:1200px;height:532px;background:var(--cream)}
.product h2{position:absolute;left:147px;top:128px;font-size:27px;line-height:33px;font-weight:500;color:var(--ink)}
.coverage{position:absolute;left:147px;top:220px;display:flex;align-items:center;gap:12px;font-size:13px;font-weight:500;color:var(--ink)}
.product p{position:absolute;left:147px;top:267px;width:390px;font-size:13px;line-height:21.5px}
.bar{position:absolute;background:var(--yellow)}
.product-photo{position:absolute;left:565px;top:240px;width:480px;height:280px;border-radius:16px;background:linear-gradient(160deg,#e9e9e9 0%,#bdbdbd 40%,#4a4a4a 75%,#2a2a2a 100%);box-shadow:0 14px 30px rgba(0,0,0,.18);z-index:2}
/* featured */
.featured{position:absolute;left:0;top:1662px;width:1200px;height:238px;background:var(--yellow)}
.featured h2{position:absolute;left:0;width:1200px;top:34px;text-align:center;font-size:26px;font-weight:500;color:var(--ink)}
.feature{position:absolute;top:106px;display:flex;align-items:center;gap:12px;font-size:16.5px;line-height:20px;color:var(--ink)}
/* case studies */
.cases-title{position:absolute;left:0;width:1200px;top:1972px;text-align:center;font-size:28px;font-weight:500;color:var(--ink)}
.case{position:absolute;top:2037px;width:300px}
.case .photo{width:283px;height:193px}
.case h3{font-size:20px;line-height:24px;font-weight:500;color:var(--ink);margin-top:15px}
.case p{font-size:13px;line-height:21.5px;margin-top:12px;width:262px}
/* contact */
.contact{position:absolute;left:0;top:2510px;width:1200px;height:532px;background:linear-gradient(120deg,#4c4a45 0%,#3a3833 40%,#5d5a52 70%,#2f2d29 100%)}
.contact h2{position:absolute;left:147px;top:174px;width:380px;font-size:27px;line-height:33px;font-weight:500;color:var(--white)}
.contact p{position:absolute;left:147px;top:287px;width:370px;font-size:13px;line-height:21.5px;color:#f2f2f2}
.contact-info{position:absolute;left:383px;top:428px;font-size:12.5px;font-weight:700;color:var(--white);letter-spacing:.2px}
.form-card{position:absolute;left:637px;top:47px;width:389px;height:421px;background:var(--white);border-radius:20px}
.field{position:absolute;left:40px;width:309px;background:var(--field);font-size:12.5px;color:#a9a9a9;padding:12px 18px}
/* footer */
.site-footer{position:absolute;left:0;top:3042px;width:1200px;height:203px;background:var(--footer);color:var(--white)}
.footer-brand{position:absolute;left:147px;top:40px;display:flex;flex-direction:column;gap:12px}
.footer-brand .mark{width:26px;height:26px;background:var(--yellow)}
.footer-brand .name{font-size:24px;font-weight:700;white-space:nowrap}
.contact-line{position:absolute;left:383px;display:flex;align-items:center;gap:12px;font-size:14px}
.footer-nav a{position:absolute;left:689px;font-size:12.5px;color:var(--white);text-decoration:none}
.social{position:absolute;top:42px;width:15px;height:15px;border-radius:50%;background:var(--white)}
</style>
</head>
<body>

<header class="site-header">
  <div class="brand-card"><div class="brand-mark"></div><div class="brand-name">Open meadow</div></div>
  <nav class="main-nav">
    <a href="#" class="active" style="left:519px">HOME</a>
    <a href="#" style="left:584px">SOLUTIONS</a>
    <a href="#" style="left:687px">CASE STUDIES</a>
    <a href="#" style="left:808px">CONTACT US</a>
  </nav>
  <a class="btn" style="left:943px;top:21px;width:104px;height:32px">GET A QUOTE</a>
</header>

<section class="hero">
  <div class="hero-photo" role="img" aria-label="Smiling woman talking on a mobile phone at home"></div>
  <h1>Enjoy Your Life Without<br>Dropped Calls</h1>
  <p>Lorem ipsum dolor sit amet consectetur. Amet tempus commodo eu eget id. Iaculis tincidunt tristique id etiam.</p>
  <a class="btn btn-outline" style="left:147px;top:326px;width:105px;height:33px">GET A QUOTE</a>
</section>

<article class="service-card" style="left:227px">
  <svg width="40" height="40" viewBox="0 0 40 40" style="margin-top:26px" fill="none" stroke="#fcc400" stroke-width="2.2" stroke-linejoin="round"><path d="M5 19 20 6l15 13"/><path d="M9 16v17h22V16"/><path d="M17 33v-9h6v9"/></svg>
  <h3>Residential</h3>
  <p>Lorem ipsum dolor sit amet consectetur. Lacinia pellentesque consectetur elementum pellentesque augue sit.</p>
</article>
<article class="service-card" style="left:580px">
  <svg width="40" height="40" viewBox="0 0 40 40" style="margin-top:31px" fill="none" stroke="#fcc400" stroke-width="2"><rect x="10" y="8" width="20" height="28"/><path d="M13 5h14v3M14 13h12M14 18h12M14 23h12M14 28h12"/></svg>
  <h3>Commercial</h3>
  <p>Lorem ipsum dolor sit amet consectetur. Lacinia pellentesque consectetur elementum pellentesque augue sit.</p>
</article>

<section class="about">
  <div class="about-logo"><div class="mark"></div><div class="name">Open meadow</div></div>
  <div class="eyebrow">ABOUT US</div>
  <h2>Lorem ipsum dolor sit amet consectetur. Hendrerit id nunc.</h2>
  <p>Lorem ipsum dolor sit amet consectetur. Lacinia pellentesque consectetur elementum pellentesque augue sit. Porttitor purus massa convallis ornare. Feugiat elit augue porttitor diam. Mi convallis nibh posuere mauris.<br>Elit porttitor ac ut tempus ac bibendum nibh. Non vitae cursus quis leo. Nisi vel eget eget porttitor dolor sem duis. Enim platea pharetra ac ut ornare est. Quam mi.</p>
</section>

<section class="product">
  <div class="bar" style="left:612px;top:67px;width:112px;height:465px"></div>
  <div class="bar" style="left:737px;top:128px;width:113px;height:404px"></div>
  <div class="bar" style="left:862px;top:187px;width:114px;height:345px"></div>
  <div class="product-photo" role="img" aria-label="Signal booster unit with indoor antennas and coiled cables"></div>
  <h2>FieldLine NextG<br>Signal Booster</h2>
  <div class="coverage">
    <svg width="22" height="20" viewBox="0 0 22 20" fill="#1b1b1b"><rect x="0" y="12" width="3.5" height="8"/><rect x="6" y="8" width="3.5" height="12"/><rect x="12" y="4" width="3.5" height="16"/><rect x="18" y="0" width="3.5" height="20"/></svg>
    Coverage: up to 300 sqm
  </div>
  <p>Lorem ipsum dolor sit amet consectetur. Lacinia pellentesque consectetur elementum pellentesque augue sit. Porttitor purus massa convallis ornare. Feugiat elit augue porttitor diam. Mi convallis nibh posuere mauris.</p>
  <a class="btn" style="left:149px;top:391px;width:105px;height:33px">GET A QUOTE</a>
</section>

<section class="featured">
  <h2>Featured</h2>
  <div class="feature" style="left:189px">
    <svg width="52" height="48" viewBox="0 0 52 48" fill="none" stroke="#1b1b1b" stroke-width="2"><path d="M6 4c10 0 16 8 16 16 0 4-2 6-2 9l4 3-3 2 1 5c0 3-3 4-7 3l-1 5H5"/><path d="M32 30v6M37 26v14M42 30v6M47 32v2"/></svg>
    <span>Crystal Clear<br>Voice Calls</span>
  </div>
  <div class="feature" style="left:403px">
    <svg width="40" height="40" viewBox="0 0 40 40" fill="none" stroke="#1b1b1b" stroke-width="2"><rect x="2" y="2" width="36" height="36" rx="4"/><path d="M12 28 28 12M18 12h10v10M12 18v10h10"/></svg>
    <span>Full Coverage In<br>Your Property</span>
  </div>
  <div class="feature" style="left:636px">
    <svg width="40" height="40" viewBox="0 0 40 40" fill="none" stroke="#1b1b1b" stroke-width="2.2"><circle cx="20" cy="20" r="17"/><path d="M13 28 31 10"/><path d="M9 22a11 11 0 0 1 14-11"/></svg>
    <span>Faster Data<br>Speeds</span>
  </div>
  <div class="feature" style="left:831px">
    <svg width="42" height="36" viewBox="0 0 42 36" fill="none" stroke="#1b1b1b" stroke-width="2" stroke-linejoin="round"><rect x="2" y="14" width="7" height="18"/><path d="M9 16l8-12c3 0 4 2 3 6l-2 5h14c2 0 3 2 2 4l-3 11c-1 2-2 2-4 2H9"/><path d="M30 4l4-3M33 9h5M31 6l6-1"/></svg>
    <span>Easy to use</span>
  </div>
</section>

<h2 class="cases-title">Case Studies</h2>
<article class="case" style="left:160px">
  <div class="photo" role="img" aria-label="Woman on a phone call at her desk" style="background:linear-gradient(135deg,#d8d2c6,#8d9fb8 60%,#6b5e52)"></div>
  <h3>Lorem ipsum dolor sit amet consectetur.</h3>
  <p>Lorem ipsum dolor sit amet consectetur. Lacinia pellentesque consectetur elementum</p>
  <a class="btn" style="left:0;top:334px;width:105px;height:32px">LEARN MORE</a>
</article>
<article class="case" style="left:457px">
  <div class="photo" role="img" aria-label="Finger dialling on a smartphone keypad" style="background:linear-gradient(135deg,#7fc4e4,#cfe8f3 50%,#a9c7d6)"></div>
  <h3 style="padding-left:9px">Lorem ipsum dolor sit amet consectetur.</h3>
  <p style="margin-left:9px">Lorem ipsum dolor sit amet consectetur. Lacinia pellentesque consectetur elementum</p>
  <a class="btn" style="left:9px;top:334px;width:105px;height:32px">LEARN MORE</a>
</article>
<article class="case" style="left:754px">
  <div class="photo" role="img" aria-label="Woman using a smartphone at a table" style="background:linear-gradient(135deg,#4c6a5c,#d9dde2 50%,#9db3cc)"></div>
  <h3 style="padding-left:5px">Lorem ipsum dolor sit amet consectetur.</h3>
  <p style="margin-left:5px">Lorem ipsum dolor sit amet consectetur. Lacinia pellentesque consectetur elementum</p>
  <a class="btn" style="left:5px;top:334px;width:105px;height:32px">LEARN MORE</a>
</article>

<section class="contact" role="img" aria-label="Hands holding a smartphone, darkened background">
  <h2>Are you unsure if a mobile signal booster will work for you? Let us help.</h2>
  <p>Lorem ipsum dolor sit amet consectetur. Lacinia pellentesque consectetur elementum pellentesque augue sit. Porttitor purus massa convallis ornare. Feugiat elit augue porttitor diam. Mi convallis nibh posuere mauris. Elit porttitor ac ut tempus ac bibendu</p>
  <a class="btn" style="left:147px;top:423px;width:104px;height:32px">GET A SIGNAL</a>
  <div class="contact-info">CONTACT INFORMATIONS</div>
  <form class="form-card">
    <div class="field" style="top:33px;height:38px">Full name</div>
    <div class="field" style="top:94px;height:39px">Phone</div>
    <div class="field" style="top:152px;height:39px;width:311px">Email</div>
    <div class="field" style="top:209px;height:106px;width:311px">Write to us</div>
    <div class="btn" style="left:38px;top:343px;width:141px;height:34px;border:none;border-radius:17px;font-size:12.5px">SEND</div>
  </form>
</section>

<footer class="site-footer">
  <div class="footer-brand"><div class="mark"></div><div class="name">Open meadow</div></div>
  <div class="contact-line" style="top:67px">
    <svg width="17" height="19" viewBox="0 0 17 19" fill="none" stroke="#fff" stroke-width="1.6"><path d="M8.5 18s6.5-6 6.5-10.5a6.5 6.5 0 0 0-13 0C2 12 8.5 18 8.5 18z"/><circle cx="8.5" cy="7.5" r="2.3"/></svg>
    Your locations
  </div>
  <div class="contact-line" style="top:100px">
    <svg width="17" height="14" viewBox="0 0 17 14" fill="none" stroke="#fff" stroke-width="1.6"><rect x="1" y="1" width="15" height="12" rx="1.5"/><path d="M1 2l7.5 6L16 2"/></svg>
    Info@openmeadow.com
  </div>
  <div class="contact-line" style="top:134px">
    <svg width="17" height="17" viewBox="0 0 17 17" fill="none" stroke="#fff" stroke-width="1.6" stroke-linejoin="round"><path d="M4 1.5 6.5 5 5 7a10 10 0 0 0 5 5l2-1.5 3.5 2.5-1.5 2.5C9 16 1 8 1.5 3z"/></svg>
    +46-701234560
  </div>
  <nav class="footer-nav">
    <a href="#" style="top:64px">HOME</a>
    <a href="#" style="top:87px">SOLUTIONS</a>
    <a href="#" style="top:114px">CASE STUDIES</a>
    <a href="#" style="top:142px">CONTACT US</a>
  </nav>
  <span class="social" style="left:912px"></span>
  <span class="social" style="left:938px"></span>
  <span class="social" style="left:964px"></span>
  <span class="social" style="left:990px"></span>
  <span class="social" style="left:1016px"></span>
</footer>

</body>
</html>
```